Not Your Average Diet Book Cover Design

I need a book cover designed for a project titled:
Title: Table Route Junction
Sub-title: The Hidden Key To Gently Mastering Your Meals
Author: Carla Brightwood
Designation: Not a Doctor
The book is a look at 8 trendy diets (Carbwise, Whole Foods, Paleo, Keto, Mediterranean, Sugar Free, Alkaline and Intermittent Fasting), with each chapter covering the pros and cons of one.
The theme throughout the book is that, when approached as a diet, they are each doomed to failure. When sustainability and lifestyle are taken into consideration, however, any one of them (or a combination of two or more) can lead to overall health and weight management.
Vegetables, mindset and habit creation are 3 of the "overlap" factors implied in the title.
I have uploaded a temporary cover that I am using as a placeholder at the moment. I do NOT want anything like it. (Use the tagline above, not the one in the sample cover).
Please, NO images of scales, stomachs, or anything else that is super cliche for the weight loss industry.
This is a full length book, written in a conversation tone, that I want to stand out from the a) copy and pasted online "experts" and b) doctors and fitpros who think it's their way or the highway. I want it to be welcoming and accessible.
I want the book to appeal to an audience who is currently struggling with their health and most likely failed at many diets in the past.
I will need a print cover for a 6"x 9" Pressbloom book, as well as a Lumora cover and an Sonvera cover.
I would like all source files, including any fonts used. For delivery, placeholder text can be used for the back cover.
Target Market(s)
Male & Female
Overweight
Unhealthy, but not severely so
Have tried diets before and failed
Age: 25-55 (average)
Income: $30-50k USD
Marital status: Single OR not entirely satisfied with the relationship
Location: Canada, USA, Australia, UK
Industry/Entity Type
Health And Wellness
Colors
Designer to choose colors to be used in the design.
Requirements
Must have
- Title: Table Route Junction
- Sub-title: The Hidden Key To Gently Mastering Your Meals
- Author: Carla Brightwood
- Designation: Not a Doctor
Nice to have
- A welcoming, understanding feeling
- Implications of holistic health
Should not have
- Images:
- - Scale or measuring tapes, etc
- - stomachs/abs
- - yoga or any silhouettes
- A look similar to the sample.

```html
<!DOCTYPE html>
<html lang="en">
<head>
<meta charset="utf-8">
<title>Table Route Junction — Book Cover</title>
<link href="https://fonts.googleapis.com/css2?family=Bebas+Neue&family=Anton&family=Montserrat:wght@300&family=Open+Sans:wght@400;600&family=Arimo:ital,wght@1,700&display=swap" rel="stylesheet">
<style>
  :root {
    --page: #ffffff;
    --yellow: #f3c92c;
    --yellow-deep: #eebf22;
    --ink: #2e3437;
    --blue: #0b4fa6;
    --body-grey: #7b7663;
    --quote-mark: #f1ede2;
  }
  * { margin: 0; padding: 0; box-sizing: border-box; }
  html, body { width: 1200px; height: 917px; overflow: hidden; background: var(--page); }
  .canvas { position: relative; width: 1200px; height: 917px; }
  .cover {
    position: absolute; left: 106px; top: 108px; width: 968px; height: 686px;
    background: linear-gradient(135deg, var(--yellow) 0%, var(--yellow-deep) 100%);
    overflow: hidden;
    box-shadow: 2px 3px 5px rgba(0,0,0,.35);
  }
  .cover-art { position: absolute; inset: 0; }
  .back-copy {
    position: absolute; left: 65px; top: 188px; width: 334px;
    font-family: "Montserrat", sans-serif; font-weight: 300;
    font-size: 15.6px; line-height: 20px; letter-spacing: 0.35px; color: var(--body-grey);
    text-align: justify; hyphens: auto;
  }
  .back-copy p + p { margin-top: 20px; }
  .quote-mark {
    position: absolute; font-family: "Anton", sans-serif;
    font-size: 118px; line-height: 1; color: var(--quote-mark);
  }
  .quote-open { left: 62px; top: 100px; }
  .quote-close { left: 338px; top: 452px; }
  .spine-title, .spine-author {
    position: absolute; color: var(--blue); white-space: nowrap;
    transform: rotate(-90deg); transform-origin: left top;
  }
  .spine-title {
    left: 460px; top: 654px;
    font-family: "Bebas Neue", sans-serif; font-size: 58px; line-height: 46px;
  }
  .spine-author {
    left: 472px; top: 226px;
    font-family: "Open Sans", sans-serif; font-size: 27px; line-height: 30px;
  }
  .front-subtitle {
    position: absolute; left: 562px; top: 270px; width: 352px; height: 21px;
    background: rgba(255,255,255,.35);
    font-family: "Arimo", sans-serif; font-style: italic; font-weight: 700;
    font-size: 14.4px; line-height: 21px; color: var(--blue); text-align: center;
    white-space: nowrap;
  }
  .front-author {
    position: absolute; left: 534px; top: 584px; width: 400px; text-align: center;
    font-family: "Open Sans", sans-serif; color: var(--blue);
  }
  .front-author .name { font-weight: 600; font-size: 29px; line-height: 36px; }
  .front-author .designation { font-size: 16px; line-height: 20px; }
</style>
</head>
<body>
<div class="canvas">
  <div class="cover">
    <svg class="cover-art" width="968" height="686" viewBox="0 0 968 686">
      <defs>
        <radialGradient id="plateTone" cx="0.55" cy="0.5" r="0.6">
          <stop offset="0" stop-color="#f1f2f3"/>
          <stop offset="1" stop-color="#dcdddf"/>
        </radialGradient>
        <linearGradient id="forkTone" x1="0" x2="1">
          <stop offset="0" stop-color="#9c9c9a"/>
          <stop offset="0.5" stop-color="#dcdcda"/>
          <stop offset="1" stop-color="#8e8e8c"/>
        </linearGradient>
        <clipPath id="overlapClip"><polygon points="700,130 968,130 968,270 728,270"/></clipPath>
      </defs>
      <circle class="plate" cx="934" cy="452" r="298" fill="url(#plateTone)" role="img" aria-label="Photograph of an empty white dinner plate"/>
      <rect class="fork" x="562" y="230" width="50" height="440" rx="20" fill="url(#forkTone)" opacity=".85" role="img" aria-label="Photograph of a silver dinner fork"/>
      <g class="front-title" font-family="Bebas Neue, sans-serif" fill="var(--ink)">
        <text x="550" y="142" font-size="98" textLength="370" lengthAdjust="spacingAndGlyphs">TABLE ROUTE</text>
        <text x="548" y="256" font-size="136" textLength="372" lengthAdjust="spacingAndGlyphs">JUNCTION</text>
      </g>
      <g class="front-title-overlap" font-family="Bebas Neue, sans-serif" fill="var(--blue)" clip-path="url(#overlapClip)" aria-hidden="true">
        <text x="548" y="256" font-size="136" textLength="372" lengthAdjust="spacingAndGlyphs">JUNCTION</text>
      </g>
    </svg>

    <div class="quote-mark quote-open" aria-hidden="true">“</div>
    <div class="back-copy">
      <p>The book is a look at 8 trendy diets (Carbwise, Whole Foods, Paleo, Keto, Mediterranean, Sugar Free, Alkaline and Intermittent Fasting), with each chapter covering the pros and cons of one.</p>
      <p>The theme throughout the book is that, when approached as a diet, they are each doomed to failure. When sustainability and lifestyle are taken into consideration, however, any one of them (or a combination of two or more) can lead to overall health and weight management.</p>
    </div>
    <div class="quote-mark quote-close" aria-hidden="true">”</div>

    <div class="spine-title">TABLE ROUTE JUNCTION</div>
    <div class="spine-author">Carla Brightwood</div>

    <div class="front-subtitle">The Hidden Key To Gently Mastering Your Meals</div>
    <div class="front-author">
      <div class="name">Carla Brightwood</div>
      <div class="designation">Not a Doctor</div>
    </div>
  </div>
</div>
</body>
</html>
```